High-end Packaging Design For Permanent Holiday Lights

We need a design for our product box for our company HaloSpan which sells permanent Christmas lights.
Box dimensions: 12.69 X 12.69 X 2.06
The box contains a starter kit and lights for customers who want to install their own permanent holiday lights. We want to see classy minimalistic designs the incorporate our logo and brand guidelines.

More white space and use of our logo.

Do not use random imagines of Christmas lights or weird shapes for the design.

This should mimic the style of an orvane zumrik packaging or high end laptop etc.

Target Market(s)

35+ men and women who love the holidays

Industry/Entity Type

Holiday lights

Font styles to use
Other font styles liked:
• Gotham

Requirements
Must have
• Must have our logo, must be classy/high end, must give multiple color options.
Nice to have
• Possible raised foil logo, or different ideas for our logo elements, play around with layouts for the box dimensions.
Should not have
• shouldn't contain any Christmas design elements as our product is used year round,

```html
<!DOCTYPE html>
<html lang="en">
<head>
<meta charset="utf-8">
<title>HaloSpan – Packaging Dieline</title>
<link rel="stylesheet" href="https://fonts.googleapis.com/css2?family=Barlow+Condensed:wght@600;700&family=Barlow:wght@500&family=Montserrat:wght@500&display=swap">
<style>
  :root {
    --canvas: #e8e9eb;
    --panel-deep: #1a0f36;
    --panel-mid: #3b1d72;
    --panel-glow: #6a2ea0;
    --glow-pink: rgba(232, 60, 160, 0.35);
    --glow-blue: rgba(90, 110, 255, 0.30);
    --tag-yellow: #fbbd26;
    --tag-blue: #3b5bc9;
    --accent-pink: #ec3a93;
    --pill-blue: #2b3592;
    --white: #ffffff;
    --dieline: #1c1c1c;
    --fold: rgba(255, 255, 255, 0.55);
  }
  * { margin: 0; padding: 0; box-sizing: border-box; }
  html, body { width: 1200px; height: 688px; overflow: hidden; background: var(--canvas); }
  .canvas { position: relative; width: 1200px; height: 688px; }

  .flaps { position: absolute; left: 0; top: 0; }

  .carton {
    position: absolute; top: 170px; width: 526px; height: 452px;
    box-shadow: 3px 3px 4px rgba(0,0,0,0.35);
  }
  .carton--a { left: 74.5px; }
  .carton--b { left: 600.3px; }

  .artwork {
    position: absolute; inset: 0;
    background:
      radial-gradient(ellipse 60% 22% at 62% 20%, var(--glow-pink), transparent 70%),
      radial-gradient(ellipse 70% 18% at 45% 85%, var(--glow-pink), transparent 70%),
      radial-gradient(ellipse 55% 40% at 60% 55%, var(--glow-blue), transparent 75%),
      radial-gradient(ellipse 80% 70% at 60% 50%, var(--panel-glow), transparent 80%),
      linear-gradient(160deg, var(--panel-deep) 0%, var(--panel-mid) 55%, var(--panel-deep) 100%);
  }

  .fold { position: absolute; top: 0; bottom: 0; left: 73px; width: 1px; background: var(--fold); }

  .side-panel { position: absolute; left: 0; top: 0; width: 73px; height: 100%; }
  .side-label {
    position: absolute; top: 43px;
    writing-mode: vertical-rl;
    font-family: "Barlow Condensed", sans-serif; font-weight: 700;
    font-size: 19px; color: var(--white); letter-spacing: 0.3px; line-height: 1;
  }
  .side-label--name { left: 38px; }
  .side-label--length { left: 13px; }

  .front-panel { position: absolute; left: 73px; top: 0; width: 453px; height: 100%; }

  .length-tag { position: absolute; left: 359px; top: 0; width: 73px; height: 89px; }
  .length-tag__value {
    position: absolute; left: 0; top: 43px; width: 73px; text-align: center;
    font-family: "Barlow Condensed", sans-serif; font-weight: 700;
    font-size: 29px; color: var(--tag-blue); line-height: 1;
  }
  .feature {
    position: absolute; left: 352px; top: 94px; width: 87px; text-align: center;
    font-family: "Barlow Condensed", sans-serif; font-weight: 700;
    font-size: 19px; line-height: 21px; color: var(--accent-pink);
  }

  .brand-name {
    position: absolute; left: 0; width: 453px; top: 415px; text-align: center;
    font-family: "Montserrat", sans-serif; font-weight: 500;
    font-size: 31px; letter-spacing: 7px; color: var(--white); line-height: 1;
  }
  .brand-name { top: 245px; }

  .tagline {
    position: absolute; left: 48px; top: 293.5px; width: 356px; height: 33px;
    border-radius: 17px; background: var(--pill-blue);
    display: flex; align-items: center; justify-content: center;
    font-family: "Barlow", sans-serif; font-weight: 500;
    font-size: 16px; letter-spacing: 0.3px; color: var(--white);
  }

  .product-spec {
    position: absolute; right: 24px; top: 370px; text-align: right;
    font-family: "Barlow Condensed", sans-serif; font-weight: 700;
    font-size: 21px; line-height: 28px; color: var(--white);
  }
</style>
</head>
<body>
<main class="canvas">

  <svg class="flaps" width="1200" height="688" viewBox="0 0 1200 688" aria-hidden="true">
    <path d="M147.6 170 V127 Q147.6 106 168.6 106 H579.3 Q600.3 106 600.3 127 V170" fill="#fff" stroke="var(--dieline)" stroke-width="1"/>
    <path d="M673.4 170 V127 Q673.4 106 694.4 106 H1105 Q1126 106 1126 127 V170" fill="#fff" stroke="var(--dieline)" stroke-width="1"/>
  </svg>

  <section class="carton carton--a">
    <div class="artwork" role="img" aria-label="Glowing purple, pink and gold light-trail swirl background"></div>
    <div class="fold"></div>
    <div class="side-panel">
      <span class="side-label side-label--name">LED STRIP LIGHT</span>
      <span class="side-label side-label--length">24.6FTX2</span>
    </div>
    <div class="front-panel">
      <svg class="length-tag" viewBox="0 0 73 89" aria-hidden="true">
        <path d="M0 0 H73 V89 L36.5 80 L0 89 Z" fill="var(--tag-yellow)"/>
      </svg>
      <span class="length-tag__value">50FT</span>
      <p class="feature">COLOR<br>CHANGING</p>
      <h1 class="brand-name">HALOSPAN</h1>
      <p class="tagline">PERMANENT CHRISTMAS LIGHTS</p>
      <p class="product-spec">LED STRIP LIGHT<br>24.6FTX2</p>
    </div>
  </section>

  <section class="carton carton--b">
    <div class="artwork" role="img" aria-label="Glowing purple, pink and gold light-trail swirl background"></div>
    <div class="fold"></div>
    <div class="side-panel">
      <span class="side-label side-label--name">LED STRIP LIGHT</span>
      <span class="side-label side-label--length">24.6FTX2</span>
    </div>
    <div class="front-panel">
      <svg class="length-tag" viewBox="0 0 73 89" aria-hidden="true">
        <path d="M0 0 H73 V89 L36.5 80 L0 89 Z" fill="var(--tag-yellow)"/>
      </svg>
      <span class="length-tag__value">50FT</span>
      <p class="feature">COLOR<br>CHANGING</p>
      <h2 class="brand-name">HALOSPAN</h2>
      <p class="tagline">PERMANENT CHRISTMAS LIGHTS</p>
      <p class="product-spec">LED STRIP LIGHT<br>24.6FTX2</p>
    </div>
  </section>

</main>
</body>
</html>
```